Stationary & Business cards for Onsite Wastewater Company
Brindlecove Septic Systems Ltd.
Stationary & Business cards for Onsite Wastewater Company - Construction
Creative Brief
Professional
Dwight Amberole
6172 Pellworth St. Langley, B.C. V3K8R2
dwight@brindlecoveseptic-example.com
brindlecoveseptic-example.com
I would like it to say: Design & Build on the front of the card
Open to ideas: maybe use the logo with black background
lanternmoth lanternmoth

```html
<!DOCTYPE html>
<html lang="en">
<head>
<meta charset="utf-8">
<title>Brindlecove Septic Systems Ltd. — Business Card</title>
<link rel="stylesheet" href="https://fonts.googleapis.com/css2?family=Open+Sans:wght@400;700;800&family=Tinos&display=swap">
<style>
  :root {
    --bg: #d9d9d9;
    --card-white: #f7f7f7;
    --card-black: #0b0b0b;
    --ink: #1d1d1d;
    --ink-soft: #555;
    --accent: #1f7fc1;
    --accent-dark: #15578a;
    --rule: #2a2a2a;
    --silver: #d0d4d8;
  }
  * { margin: 0; padding: 0; box-sizing: border-box; }
  html, body { width: 1200px; height: 842px; overflow: hidden; }
  body {
    background: var(--bg);
    font-family: "Open Sans", Arial, sans-serif;
    position: relative;
  }
  .card {
    position: absolute;
    width: 540px;
    height: 309px;
    border-radius: 3px;
    overflow: hidden;
    box-shadow: 0 6px 18px rgba(0,0,0,0.22);
  }
  .card--front { left: 70px; top: 440px; background: var(--card-white); }
  .card--back {
    left: 600px; top: 100px; background: var(--card-black);
    display: flex; align-items: center; justify-content: center;
  }

  .wordmark {
    font-family: "Open Sans", Arial, sans-serif;
    font-weight: 800;
    text-transform: uppercase;
    line-height: 1.05;
    letter-spacing: 0.5px;
  }
  .wordmark__name { display: block; font-size: 30px; }
  .wordmark__tag { display: block; font-size: 16.5px; letter-spacing: 1.6px; }

  .card--front .wordmark { position: absolute; left: 34px; top: 30px; color: var(--ink); }
  .card--back .wordmark { color: var(--silver); text-align: left; }

  .contact {
    position: absolute; left: 34px; top: 100px;
    font-size: 11px; line-height: 1.5; color: var(--ink-soft);
    font-style: normal;
  }

  .person {
    position: absolute; right: 34px; top: 198px; width: 230px;
    font-family: "Tinos", "Times New Roman", serif;
    font-size: 19px; color: var(--ink);
    padding-bottom: 4px;
    border-bottom: 1.5px solid var(--rule);
  }

  .tagline {
    position: absolute; right: 34px; top: 252px;
    font-size: 13px; color: var(--ink);
  }

  .band { position: absolute; left: 0; right: 0; bottom: 0; height: 14px; }
  .band__line { position: absolute; left: 0; right: 0; top: 0; height: 2px; background: var(--silver); }
  .band__fill {
    position: absolute; left: 0; right: 0; top: 4px; bottom: 0;
    background: linear-gradient(90deg, var(--accent-dark), var(--accent));
  }
</style>
</head>
<body>

  <section class="card card--back" aria-label="Business card back">
    <div class="wordmark">
      <span class="wordmark__name">Brindlecove</span>
      <span class="wordmark__tag">Septic Systems Ltd.</span>
    </div>
  </section>

  <section class="card card--front" aria-label="Business card front">
    <div class="wordmark">
      <span class="wordmark__name">Brindlecove</span>
      <span class="wordmark__tag">Septic Systems Ltd.</span>
    </div>

    <address class="contact">
      6172 Pellworth St.<br>
      Langley, B.C. V3K8R2<br>
      Cell: 604-555-0142 Fax: 604-555-0187<br>
      Email: dwight@brindlecoveseptic-example.com<br>
      brindlecoveseptic-example.com
    </address>

    <p class="person">Dwight Amberole</p>
    <p class="tagline">Design &amp; Build</p>

    <div class="band">
      <div class="band__line"></div>
      <div class="band__fill"></div>
    </div>
  </section>

</body>
</html>
```